New high end server provider needs wordpress design

www.kv7hosting.com

Need a wordpress design for a high end server provider that provides overclocked dedicated servers for rent. We are located in Chicago but we have a presence is Virginia and Nevada for both our east and west coast customers.

We are a server provider that specializes in top end hardware with every feature designed for optimum performance. If it is not the best quality part or provides the best possible performance we don't run it. Our customers are mainly those that want the best single threaded performance possible from their hardware. We would be selling our services directly on our website via WHMCS.

We would like to see designs that are very modern and simplistic yet very attractive looking and catchy. Would prefer colors in the blues and greens and white. These colors are not necessary and I would be open to another color scheme if it looks good.

The final design should show speed and performance while being simplistic and easy on the eyes.

Logo and company name added and payment changed to guaranteed.  Looking for a wordpress template with the same pages as kv7hosting.com but with a redesigned look and feel.  

WHMCS control panel design also part of the design request.

If you have any questions please let me know!  This is just for kv7hosting.com and a main page for WHMCS (no coding just design).

Target Market(s)

IT Guru's (mostly men in their 20's to 30's)

Industry/Entity Type

Hardware

Requirements
Must have
• WHMCS panel design to fit with website theme.
Nice to have
• Main slider on home page similar to one of our other websites at www.kv7hosting.com
Should not have
• Flash or frames

```html
<!DOCTYPE html>
<html lang="en">
<head>
<meta charset="utf-8">
<title>KV7HOSTING – Overclocked High Quality Hardware</title>
<link href="https://fonts.googleapis.com/css2?family=Open+Sans:wght@300;400;600;700;800&display=swap" rel="stylesheet">
<style>
:root{
  --ink:#1d2a33;
  --muted:#6b7780;
  --navy:#0c1a24;
  --navy-2:#13293a;
  --teal:#1b8fb0;
  --sky:#2a9fd3;
  --orange:#f08d1c;
  --page:#eef1f3;
  --card:#ffffff;
  --line:#d7dde1;
  --foot-text:#9fb1bd;
}
*{box-sizing:border-box;margin:0;padding:0}
html,body{width:727px;height:1200px;overflow:hidden}
body{font-family:"Open Sans",Arial,sans-serif;color:var(--ink);background:var(--page);font-size:9px}
.canvas{position:relative;width:727px;height:1200px;overflow:hidden;background:linear-gradient(#eef1f3,#e4e9ec)}
.abs{position:absolute}
/* top bar */
.topbar{left:0;top:0;width:727px;height:26px;background:var(--navy);color:#c9d5dc;font-size:8px}
.topbar .links{left:62px;top:8px}
.topbar .contact{right:118px;top:8px}
.social{position:absolute;right:62px;top:6px;display:flex;gap:3px}
.social span{width:14px;height:14px;border-radius:2px;background:var(--teal)}
.social span:nth-child(2){background:#3b5f9c}
.social span:nth-child(3){background:#5aa7d6}
/* header */
.header{left:0;top:26px;width:727px;height:360px;background:linear-gradient(180deg,#12495b 0%,#0f3445 45%,#0d2836 100%)}
.logo{left:62px;top:40px;width:112px;height:30px;background:var(--navy);border:2px solid var(--teal);display:flex;align-items:center;justify-content:center;color:#fff;font-weight:800;font-size:13px;letter-spacing:.5px}
.tagline{left:184px;top:48px;color:#d6e6ee;font-size:11px}
/* nav */
.nav{left:62px;top:92px;width:603px;height:22px;background:#fff;display:flex;align-items:center;font-size:7.5px;font-weight:600;color:#33414a}
.nav a{padding:0 9px;height:22px;line-height:22px;text-decoration:none;color:inherit}
.nav a.active{background:var(--teal);color:#fff}
.nav .sep{width:1px;height:10px;background:var(--line)}
.search{position:absolute;right:4px;top:4px;display:flex}
.search span{width:82px;height:14px;border:1px solid var(--line);font-size:6.5px;color:#9aa;padding:2px 4px;font-weight:400}
.search b{height:14px;background:var(--teal);color:#fff;font-size:6.5px;padding:2px 6px}
/* slider */
.slider{left:62px;top:118px;width:603px;height:254px;background:#dfe6ea;border:4px solid #fff}
.slide-photo{position:absolute;inset:0;background:radial-gradient(ellipse at 40% 45%,#8fa0ac 0%,#4d5c68 45%,#1e2a33 100%)}
.badge{left:520px;top:18px;width:70px;height:70px;border-radius:50%;background:var(--teal);border:3px solid #fff;color:#fff;text-align:center;font-weight:700;line-height:1.05;padding-top:14px;font-size:9px}
.badge strong{display:block;font-size:17px}
.caption{left:0;top:186px;width:595px;height:46px;background:rgba(10,22,30,.82);padding:8px 16px;color:#fff}
.caption h2{font-size:14px;font-weight:700}
.caption p{font-size:7px;color:#c2d0d8;margin-top:3px}
.arrow{top:110px;width:16px;height:24px;background:rgba(255,255,255,.85)}
.dots{left:322px;top:366px;display:flex;gap:3px}
.dots span{width:9px;height:9px;background:#fff;border:1px solid #b9c3c9}
.dots span.on{background:var(--teal)}
/* intro heading */
.intro{left:0;top:398px;width:727px;text-align:center;font-size:12px;color:var(--ink);font-weight:600}
.intro i{font-style:normal;color:var(--teal)}
/* plans */
.plans{left:62px;top:422px;width:603px;display:flex;gap:8px}
.plan{width:196px;height:188px;background:var(--card);border:1px solid var(--line);position:relative}
.plan h3{background:linear-gradient(#1a3a4c,#0f2431);color:#fff;font-size:10px;font-weight:600;padding:9px 10px;height:32px}
.price{position:absolute;right:8px;top:16px;width:38px;height:38px;border-radius:50%;background:var(--orange);border:2px solid #fff;color:#fff;text-align:center;font-weight:700;font-size:7px;line-height:1;padding-top:7px}
.price b{display:block;font-size:13px}
.plan ul{list-style:none;padding:12px 10px 0 14px;font-size:6.8px;color:var(--muted);line-height:1.75}
.plan li::before{content:"";display:inline-block;width:3px;height:3px;background:var(--teal);margin-right:5px;vertical-align:middle}
.server-img{position:absolute;right:10px;top:64px;width:46px;height:66px;background:linear-gradient(#7d8a94,#2c3740);border-radius:2px}
.plan-actions{position:absolute;left:12px;bottom:10px;display:flex;gap:5px}
.btn{font-size:6.5px;padding:4px 8px;border:1px solid var(--line);color:var(--ink);background:#f5f7f8}
.btn.dark{background:var(--navy-2);color:#fff;border-color:var(--navy-2)}
/* info columns */
.info{left:62px;top:628px;width:603px;display:flex;gap:22px}
.col{width:186px}
.col h2{font-size:15px;font-weight:400;color:var(--ink);margin-bottom:8px}
.col h2 .hl{color:var(--sky)}
.mini-logo{width:90px;height:24px;background:var(--navy);border:2px solid var(--teal);color:#fff;font-weight:800;font-size:9px;display:flex;align-items:center;justify-content:center;margin-bottom:8px}
.why-img{width:100%;height:40px;background:linear-gradient(90deg,#2d4b5c,#6a8594);margin-bottom:8px}
.col p{font-size:6.8px;line-height:1.6;color:var(--muted)}
.col .btn{display:inline-block;margin-top:8px}
.tweet{display:flex;gap:6px;margin-bottom:8px}
.tweet .bubble{flex:1;background:var(--navy-2);color:#d0dde5;font-size:6.5px;line-height:1.5;padding:6px 8px;border-left:3px solid var(--teal)}
.tweet .bubble b{color:#fff;display:block;font-size:7px}
.tweet .dot{width:18px;height:18px;border-radius:50%;background:var(--teal);flex:none}
.follow{font-size:6.5px;color:var(--muted);display:flex;align-items:center;gap:4px}
.follow span{width:10px;height:10px;background:var(--sky);border-radius:50%}
.feed-mark{position:absolute;left:612px;top:624px;width:26px;height:26px;border-radius:50%;background:var(--sky)}
/* clients */
.clients-title{left:0;top:890px;width:727px;text-align:center;font-size:15px;color:var(--ink);font-weight:400}
.clients-title span{color:var(--sky)}
.clients-rule{top:901px;height:1px;background:var(--line);width:200px}
.clients{left:62px;top:918px;width:603px;display:flex;justify-content:space-between;align-items:center;padding:0 22px}
.client{display:flex;align-items:center;gap:4px;font-weight:700;font-size:11px;color:#2b3840}
.client i{width:8px;height:8px;background:#2b3840;display:block}
.c-arrow{top:924px;width:0;height:0;border-top:6px solid transparent;border-bottom:6px solid transparent}
/* footer */
.footer{left:0;top:958px;width:727px;height:242px;background:linear-gradient(#10222e,#0a1820);color:var(--foot-text)}
.fcol{top:14px}
.fcol h2{font-size:15px;font-weight:400;color:#fff;margin-bottom:7px}
.fcol h2 span{color:var(--sky)}
.news-item{display:flex;gap:6px;margin-bottom:6px;width:190px}
.news-item .thumb{width:26px;height:22px;background:linear-gradient(#2f5366,#17303f);flex:none}
.news-item p{font-size:6.3px;line-height:1.5}
.news-item small{display:block;color:var(--sky);font-size:6px}
.quick{list-style:none;font-size:8.5px;line-height:1.4;color:#e4edf2}
.quick li.sub{color:var(--sky)}
.touch p{font-size:7px;display:flex;align-items:center;gap:6px;margin-bottom:5px}
.touch .ic{width:14px;height:14px;border-radius:50%;background:var(--teal);flex:none;display:flex;align-items:center;justify-content:center}
.newsletter{margin-top:8px}
.newsletter p{font-size:6.5px;margin-bottom:5px}
.nl-row{display:flex}
.nl-row span{width:120px;height:16px;background:#fff;font-size:6.5px;color:#98a4ab;padding:3px 5px}
.nl-row b{height:16px;background:var(--teal);color:#fff;font-size:6.5px;padding:3px 7px}
.follow-foot{font-size:7px;color:var(--sky);display:flex;align-items:center;gap:5px}
.follow-foot span{width:12px;height:12px;border-radius:50%;background:var(--sky)}
.bottombar{left:0;top:1178px;width:727px;height:22px;background:#07121a;font-size:6.5px;color:#7d8f9a}
.bottombar .copy{left:62px;top:7px}
.bottombar .top{right:62px;top:4px;display:flex;align-items:center;gap:4px}
.bottombar .top span{width:14px;height:14px;background:var(--teal)}
</style>
</head>
<body>
<div class="canvas">

  <div class="abs topbar">
    <div class="abs links">About us &nbsp;|&nbsp; Game Servers &nbsp;|&nbsp; Buy KV7 &nbsp;|&nbsp; SiteMap</div>
    <div class="abs contact">Email: hello@kv7hosting.com &nbsp;&nbsp; Call: +1 555-014-2290</div>
    <div class="social"><span></span><span></span><span></span></div>
  </div>

  <div class="abs header"></div>
  <div class="abs logo">KV7HOSTING</div>
  <div class="abs tagline">Overclocked High Quality Hardware</div>

  <nav class="abs nav">
    <a class="active">HOME</a>
    <a>GAME SERVERS</a><span class="sep"></span>
    <a>DEDICATED SERVERS</a><span class="sep"></span>
    <a>WHY KV7?</a><span class="sep"></span>
    <a>TESTIMONIALS</a><span class="sep"></span>
    <a>FAQ</a><span class="sep"></span>
    <a>CONTACT</a>
    <div class="search"><span>Search here</span><b>SEARCH</b></div>
  </nav>

  <section class="abs slider">
    <div class="slide-photo" role="img" aria-label="Close-up photo of an overclocked server motherboard with cooling hardware"></div>
    <div class="abs badge">Just<strong>$45</strong>/Month</div>
    <div class="abs caption">
      <h2>Overclocked High Quality Hardware</h2>
      <p>Our hardware is top of the line running overclocked Corelux Pro 7 processors at 4.5 GHz</p>
    </div>
    <div class="abs arrow" style="left:0"></div>
    <div class="abs arrow" style="right:0"></div>
  </section>
  <div class="abs dots"><span></span><span class="on"></span><span></span><span></span><span></span></div>

  <h2 class="abs intro"><i>‹</i> Highest quality, highest performing Frontline Siege 2 servers available for rent <i>›</i></h2>

  <section class="abs plans">
    <article class="plan">
      <h3>Game Servers</h3>
      <div class="price">from<b>$27</b></div>
      <ul><li>Corelux Pro 7 X930 CPU at 4.5 GHz</li><li>16 GB of Quad Channel DDR3</li><li>Power Slots</li><li>LGCC Admin Panel</li><li>Web administration Panel</li><li>Instant Setup</li></ul>
      <div class="server-img" role="img" aria-label="Server tower"></div>
      <div class="plan-actions"><span class="btn dark">Order Now</span><span class="btn">More Info</span></div>
    </article>
    <article class="plan">
      <h3>Dedicated Servery</h3>
      <div class="price">from<b>$36</b></div>
      <ul><li>Corelux Pro 7 X930 CPU at 4.5 GHz</li><li>16 GB of Quad Channel DDR3</li><li>Power Slots</li><li>LGCC Admin Panel</li><li>Web administration Panel</li><li>Instant Setup</li></ul>
      <div class="server-img" role="img" aria-label="Server tower"></div>
      <div class="plan-actions"><span class="btn dark">Order Now</span><span class="btn">More Info</span></div>
    </article>
    <article class="plan">
      <h3>Frontline Siege 2 servers</h3>
      <div class="price">from<b>$45</b></div>
      <ul><li>Corelux Pro 7 X930 CPU at 4.5 GHz</li><li>16 GB of Quad Channel DDR3</li><li>Power Slots</li><li>LGCC Admin Panel</li><li>Web administration Panel</li><li>Instant Setup</li></ul>
      <div class="server-img" role="img" aria-label="Server tower"></div>
      <div class="plan-actions"><span class="btn dark">Order Now</span><span class="btn">More Info</span></div>
    </article>
  </section>

  <section class="abs info">
    <div class="col">
      <h2><span class="hl">Who</span> we are?</h2>
      <div class="mini-logo">KV7HOSTING</div>
      <p>KV7hosting is a server provider that offers the highest quality, highest performing game and dedicated servers for rent. Our servers are custom built for demanding players.</p>
      <span class="btn dark">Read More</span>
    </div>
    <div class="col">
      <h2>Why <span class="hl">KV7?</span></h2>
      <div class="why-img" role="img" aria-label="Photo of server hardware rack"></div>
      <p>KV7hosting was created with one goal in mind: to offer high quality, high performance servers. We only offer tuned hardware with instant setup and support.</p>
      <span class="btn dark">Read More</span>
    </div>
    <div class="col">
      <h2><span class="hl">Chirper</span> Feed</h2>
      <div class="tweet"><div class="bubble"><b>New location is online</b>Our new Nevada location now serves west coast players.</div><span class="dot"></span></div>
      <div class="tweet"><div class="bubble"><b>Upgrading to next level</b>All servers now run fresh hardware for the new season.</div><span class="dot"></span></div>
      <div class="follow"><span></span>Follow @kv7hosting on Chirper</div>
    </div>
  </section>
  <div class="feed-mark"></div>

  <div class="abs clients-rule" style="left:62px"></div>
  <div class="abs clients-rule" style="left:465px"></div>
  <h2 class="abs clients-title">Our <span>Recent Client</span></h2>
  <div class="abs c-arrow" style="left:62px;border-right:7px solid #8a969d"></div>
  <div class="abs c-arrow" style="left:658px;border-left:7px solid #8a969d"></div>
  <div class="abs clients">
    <span class="client">Northwind</span>
    <span class="client"><i></i>Corelux</span>
    <span class="client">Vantrix</span>
    <span class="client">Northwind</span>
    <span class="client"><i></i>Corelux</span>
    <span class="client">Vantrix</span>
  </div>

  <footer class="abs footer">
    <div class="abs fcol" style="left:62px">
      <h2><span>Latest</span> News</h2>
      <div class="news-item"><span class="thumb"></span><p>Our new Nevada location is now online for west coast players and clans.<small>October 17, 2013</small></p></div>
      <div class="news-item"><span class="thumb"></span><p>All game servers now ship with faster memory and instant setup.<small>October 9, 2013</small></p></div>
      <div class="news-item"><span class="thumb"></span><p>Our Virginia site doubled capacity for east coast customers this month.<small>September 28, 2013</small></p></div>
      <div class="follow-foot"><span></span>Follow us on Chirper</div>
    </div>
    <div class="abs fcol" style="left:290px">
      <h2><span>Quick</span> Links</h2>
      <ul class="quick">
        <li>Game Servers</li><li>Dedicated Servers</li><li>About Us</li><li>FAQs</li><li>Testimonials</li><li>Contact</li>
        <li class="sub">Buy Frontline Siege 2</li><li class="sub">Bright Forge Studios</li><li class="sub">KV7HD</li>
      </ul>
    </div>
    <div class="abs fcol touch" style="left:465px">
      <h2><span>Get</span> in Touch</h2>
      <p><span class="ic"><svg width="8" height="8" viewBox="0 0 8 8"><path d="M1.5 1l1.5 0 .6 1.6-.9.6a4 4 0 0 0 2.1 2.1l.6-.9L7 5v1.5A.6.6 0 0 1 6.4 7 5.5 5.5 0 0 1 1 1.6.6.6 0 0 1 1.5 1z" fill="#fff"/></svg></span>+1 555-014-2290</p>
      <p><span class="ic"><svg width="8" height="6" viewBox="0 0 8 6"><rect x=".5" y=".5" width="7" height="5" fill="none" stroke="#fff"/><path d="M.5.5L4 3.5 7.5.5" fill="none" stroke="#fff"/></svg></span>hello@kv7hosting.com</p>
      <p><span class="ic"><svg width="6" height="8" viewBox="0 0 6 8"><path d="M3 8S0 4.6 0 3a3 3 0 0 1 6 0c0 1.6-3 5-3 5z" fill="#fff"/><circle cx="3" cy="3" r="1" fill="#1b8fb0"/></svg></span>120 Lake Street, Chicago</p>
      <p><span class="ic"><svg width="8" height="8" viewBox="0 0 8 8"><circle cx="4" cy="4" r="3.4" fill="none" stroke="#fff"/><path d="M.6 4h6.8M4 .6v6.8" stroke="#fff" stroke-width=".7"/></svg></span>www.kv7hosting.com</p>
      <div class="newsletter">
        <h2><span>Free</span> Newsletter</h2>
        <p>Sign up to get the latest news and offers.</p>
        <div class="nl-row"><span>Your email address</span><b>SUBSCRIBE</b></div>
      </div>
    </div>
  </footer>

  <div class="abs bottombar">
    <div class="abs copy">Copyright © 2013 KV7hosting. All Rights Reserved.</div>
    <div class="abs top"><span></span>Back to Top</div>
  </div>

</div>
</body>
</html>
```